Southport Billboard for Hiring more CDL drivers

I need a catch design for a bill board (size 10ft by 36 ft) to catch the attention for semi truck drivers.
In the design I want it to include:
-My company logo along with my website(ridgewaycarriers.com) and my number(803-555-0172) for contact info.
-I also need it to say earn up to $90,000 a year
-I will send a few photos to choose from
-I need the logo to look clean and simple! I don't want it to be cluttered just clean, simple and catchy.!

Target Market(s)

CDL Class A holders
Semi Truck Drivers

Industry/Entity Type

Trucking Company

Font styles to use
Other font styles liked:
• a font to match my logo

Requirements
Must have
• "Make up to $90,000"
"ridgewaycarriers.com"
"803-555-0172"

```html
<!DOCTYPE html>
<html lang="en">
<head>
<meta charset="utf-8">
<title>Ridgeway Carriers – Driver Hiring Billboard</title>
<link rel="stylesheet" href="https://fonts.googleapis.com/css2?family=Oswald:wght@700&display=swap">
<style>
  :root {
    --canvas: #ffffff;
    --board-dark: #252a25;
    --photo-sky: #b9bdbb;
    --photo-foliage: #4c5a44;
    --photo-truck: #b5282c;
    --brand-red: #c8262c;
    --ink-white: #ffffff;
    --text-shadow: rgba(0, 0, 0, 0.55);
  }
  * { box-sizing: border-box; margin: 0; padding: 0; }
  html, body {
    width: 1200px; height: 1200px; overflow: hidden;
    background: var(--canvas);
  }
  .billboard {
    position: absolute; left: 20px; top: 439px;
    width: 1160px; height: 322px;
    background: var(--board-dark);
    overflow: hidden;
    font-family: "Oswald", "Arial Narrow", sans-serif;
    font-weight: 700;
    color: var(--ink-white);
  }
  .truck-photo {
    position: absolute; left: 0; top: 0; width: 860px; height: 322px;
    background:
      radial-gradient(ellipse 260px 150px at 230px 210px, var(--photo-truck) 0%, rgba(181,40,44,0.75) 45%, rgba(181,40,44,0) 100%),
      linear-gradient(180deg, var(--photo-foliage) 0%, #7a8476 35%, var(--photo-sky) 55%, #5e625f 100%);
    -webkit-mask-image: linear-gradient(90deg, #000 0%, #000 55%, transparent 100%);
    mask-image: linear-gradient(90deg, #000 0%, #000 55%, transparent 100%);
  }
  .headline {
    position: absolute; left: 393px; top: 22px;
    line-height: 1;
    text-shadow: 4px 4px 6px var(--text-shadow);
    letter-spacing: -1px;
  }
  .headline-lead { display: block; font-size: 80px; }
  .headline-amount { display: block; font-size: 118px; margin-top: -4px; }
  .brand-name {
    position: absolute; left: 868px; top: 58px; width: 262px;
    text-align: center; line-height: 1.2;
    text-transform: uppercase;
    font-size: 54px; letter-spacing: 1px;
    white-space: nowrap;
  }
  .brand-name span { display: block; }
  .contact-band { position: absolute; left: 0; top: 260px; width: 1160px; height: 62px; }
  .website {
    position: absolute; left: 26px; top: 265px;
    font-size: 36px; letter-spacing: 1px;
    text-shadow: 3px 3px 4px var(--text-shadow);
  }
  .phone {
    position: absolute; right: 22px; top: 257px;
    font-size: 50px; line-height: 1.2;
  }
</style>
</head>
<body>
  <section class="billboard">
    <div class="truck-photo" role="img" aria-label="Photo of a red semi truck with a flatbed trailer parked in front of trees under a cloudy sky"></div>

    <h1 class="headline">
      <span class="headline-lead">Make up to</span>
      <span class="headline-amount">$90,000</span>
    </h1>

    <div class="brand-name" aria-label="Ridgeway Carriers">
      <span>Ridgeway</span>
      <span>Carriers</span>
    </div>

    <svg class="contact-band" viewBox="0 0 1160 62" aria-hidden="true">
      <polygon points="0,28 830,18 845,2 1160,2 1160,54 845,54 830,48 0,50" fill="var(--brand-red)" opacity="0.92"/>
    </svg>

    <p class="website">ridgewaycarriers.com</p>
    <p class="phone">803-555-0172</p>
  </section>
</body>
</html>
```